Corvale Fitouts Web

We just need an update/re-design of our existing web site that would include our new company logo and some new photo's. Our current web site can be viewed at www.corvalefitouts.com.au. We would require something very similar to what we have at the moment in terms of content it should all be the same.
The web site would basically act more as a portfolio than one that would generate more business.
We are after a very modern and simple design and maybe something where we can upload our own project photo's and project descriptions as we complete them.

```html
<!DOCTYPE html>
<html lang="en">
<head>
<meta charset="utf-8">
<title>Corvale Fitouts</title>
<link href="https://fonts.googleapis.com/css2?family=Raleway:wght@300;400&display=swap" rel="stylesheet">
<style>
:root{
  --ink:#333335;
  --muted:#a3a3a3;
  --line:#eeeeee;
  --dark:#3a3a3c;
  --icon:#2b2b2d;
  --white:#ffffff;
}
*{margin:0;padding:0;box-sizing:border-box}
html,body{width:741px;height:1200px;overflow:hidden;background:var(--white)}
body{position:relative;font-family:'Raleway',sans-serif;color:var(--ink)}
.abs{position:absolute}
.brand{font-weight:300;font-size:22px;letter-spacing:.2px;color:var(--ink);white-space:nowrap}
.nav{display:flex;gap:14px;font-size:7px;color:var(--muted);white-space:nowrap}
.nav .sep{color:var(--muted)}
.photo{position:absolute}
.section-title{position:absolute;left:0;width:741px;text-align:center;font-size:12px;font-weight:400;color:var(--ink)}
.rule{position:absolute;left:356px;width:29px;height:1.5px;background:var(--ink)}
.copy{position:absolute;left:0;width:741px;text-align:center;font-size:7px;line-height:11px;color:var(--muted)}
.divider{position:absolute;left:99px;width:543px;height:1px;background:var(--line)}
.service{position:absolute;display:flex;gap:11px}
.service .icon{width:32px;height:32px;background:var(--icon);display:flex;align-items:center;justify-content:center}
.service h3{font-size:8.5px;font-weight:400;color:var(--ink);margin-top:6px}
.service p{font-size:6px;color:var(--muted);margin-top:5px;white-space:nowrap}
.pager{position:absolute;width:15px;height:14px;border:1px solid var(--ink);display:flex;align-items:center;justify-content:center}
.footer{position:absolute;left:0;top:1082px;width:741px;height:92px;background:var(--dark)}
.footer .brand{color:var(--white)}
.footer .nav{color:var(--white)}
.social{position:absolute;width:15px;height:15px;border:1px solid var(--ink)}
.legal{position:absolute;left:99px;top:1184px;font-size:5.5px;color:var(--muted)}
</style>
</head>
<body>

<header>
  <div class="abs brand" style="left:99px;top:26px">Corvale Fitouts</div>
  <nav class="abs nav" style="right:99px;top:35px">
    <span>Home</span><span class="sep">/</span><span>Recent Projects</span><span class="sep">/</span><span>Our Services</span><span class="sep">/</span><span>Contact Us</span>
  </nav>
</header>

<section class="hero">
  <div class="photo" role="img" aria-label="Grey commercial building facade with louvres and a teal sign under a cloudy sky" style="left:99px;top:78px;width:176px;height:208px;background:linear-gradient(180deg,#c9cbcd 0%,#b5b8ba 45%,#5b5e61 70%,#3d3f42 100%)"></div>
  <div class="photo" role="img" aria-label="Modern white cantilevered office building against a grey sky" style="left:282px;top:78px;width:176px;height:208px;background:linear-gradient(160deg,#cfd1d3 0%,#b9bcbe 40%,#9ea1a4 65%,#4a4d50 100%)"></div>
  <div class="photo" role="img" aria-label="Office lobby interior with timber ceiling and patterned carpet" style="left:466px;top:78px;width:176px;height:208px;background:linear-gradient(180deg,#4a4c52 0%,#8c7a66 30%,#d7d5d0 55%,#b9b6ae 80%,#4b4f7a 100%)"></div>
</section>

<section class="about">
  <h1 class="section-title" style="top:329px">Corvale Fitouts Pty Ltd</h1>
  <div class="rule" style="top:355px"></div>
  <p class="copy" style="top:391px">Corvale Fitouts Pty Ltd was established in 2005 and has been operating in the Sydney area, but has<br>completed numerous projects outside of Sydney.</p>
  <div class="divider" style="top:433px"></div>
</section>

<section class="gallery">
  <div class="photo" role="img" aria-label="Office building with timber cladding and grey panels" style="left:99px;top:454px;width:79px;height:79px;background:linear-gradient(160deg,#cfd0d2 0%,#6c6d70 45%,#a46a3e 70%,#3f4043 100%)"></div>
  <div class="photo" role="img" aria-label="Glass facade reflecting blue sky" style="left:192px;top:454px;width:79px;height:79px;background:linear-gradient(180deg,#6f95c4 0%,#a6b9cc 35%,#3c4a5c 65%,#6b4a3a 85%,#2e2f33 100%)"></div>
  <div class="photo" role="img" aria-label="Dark blue clad office building corner" style="left:285px;top:454px;width:79px;height:79px;background:linear-gradient(170deg,#d9dadc 0%,#2e3a4e 35%,#27324a 75%,#3a3d42 100%)"></div>
  <div class="photo" role="img" aria-label="Office building with timber cladding and grey panels" style="left:377px;top:454px;width:79px;height:79px;background:linear-gradient(160deg,#cfd0d2 0%,#6c6d70 45%,#a46a3e 70%,#3f4043 100%)"></div>
  <div class="photo" role="img" aria-label="Glass facade reflecting blue sky" style="left:470px;top:454px;width:79px;height:79px;background:linear-gradient(180deg,#6f95c4 0%,#a6b9cc 35%,#3c4a5c 65%,#6b4a3a 85%,#2e2f33 100%)"></div>
  <div class="photo" role="img" aria-label="Dark blue clad office building corner" style="left:562px;top:454px;width:79px;height:79px;background:linear-gradient(170deg,#d9dadc 0%,#2e3a4e 35%,#27324a 75%,#3a3d42 100%)"></div>
  <svg class="abs" style="left:664px;top:487px" width="10" height="14" viewBox="0 0 10 14"><path d="M2 1 L8 7 L2 13" fill="none" stroke="#d0d0d0" stroke-width="2"/></svg>
</section>

<section class="services">
  <h2 class="section-title" style="top:586px">We specialise in the internal fit outs to</h2>
  <div class="rule" style="top:611px"></div>

  <div class="service" style="left:99px;top:649px">
    <div class="icon"><svg width="16" height="12" viewBox="0 0 16 12"><rect x="1" y="4" width="14" height="7" fill="#fff"/><path d="M1 4 L5 1 L9 4" fill="#fff"/><rect x="4" y="6" width="2" height="3" fill="#2b2b2d"/><rect x="9" y="6" width="3" height="2" fill="#2b2b2d"/></svg></div>
    <div><h3>Industrial Offices</h3><p>Lorem ipsum dolor sit amet, consectetur</p></div>
  </div>
  <div class="service" style="left:285px;top:649px">
    <div class="icon"><svg width="16" height="12" viewBox="0 0 16 12"><path d="M1 11 V4 L7 1 L15 4 V11 Z" fill="#fff"/><rect x="4" y="6" width="2" height="2" fill="#2b2b2d"/><rect x="9" y="6" width="4" height="2" fill="#2b2b2d"/></svg></div>
    <div><h3>Multi Storey Offices</h3><p>Lorem ipsum dolor sit amet, consectetur</p></div>
  </div>
  <div class="service" style="left:470px;top:649px">
    <div class="icon"><svg width="14" height="14" viewBox="0 0 14 14"><rect x="1" y="1" width="12" height="3" fill="#fff"/><rect x="2" y="4" width="10" height="9" fill="none" stroke="#fff" stroke-width="1.2"/><rect x="5" y="7" width="4" height="6" fill="#fff"/></svg></div>
    <div><h3>Commercial Projects</h3><p>Lorem ipsum dolor sit amet, consectetur</p></div>
  </div>
  <div class="service" style="left:99px;top:704px">
    <div class="icon"><svg width="14" height="14" viewBox="0 0 14 14"><path d="M7 1 L13 6 H11 V13 H3 V6 H1 Z" fill="#fff"/><rect x="5" y="8" width="4" height="5" fill="#2b2b2d"/></svg></div>
    <div><h3>Residential Houses</h3><p>Lorem ipsum dolor sit amet, consectetur</p></div>
  </div>
  <div class="service" style="left:285px;top:704px">
    <div class="icon"><svg width="12" height="14" viewBox="0 0 12 14"><rect x="1" y="1" width="10" height="3" fill="#fff"/><rect x="1" y="5" width="10" height="3" fill="#fff"/><path d="M1 9 H11 L6 13 Z" fill="#fff"/></svg></div>
    <div><h3>External Facades</h3><p>Lorem ipsum dolor sit amet, consectetur</p></div>
  </div>

  <p class="copy" style="top:772px">The key group of our operating staff have all been involved in the construction industry for well over 20 years.<br>Our employees are skilled and trained and have the experience to deliver the best possible product, safely and on time.<br>At Corvale Fitouts we pride ourselves on working together with our clients in providing the best possible service on schedule and within budget.</p>
</section>

<section class="projects">
  <h2 class="section-title" style="top:856px">Recent Projects</h2>
  <div class="rule" style="top:881px"></div>

  <div class="photo" role="img" aria-label="Grey commercial building with louvres and teal sign" style="left:99px;top:919px;width:126px;height:93px;background:linear-gradient(180deg,#c6c8ca 0%,#9a9da0 45%,#4d5053 75%,#3a3c3f 100%)"></div>
  <div class="photo" role="img" aria-label="Office building with timber cladding and grey panels" style="left:238px;top:919px;width:126px;height:93px;background:linear-gradient(160deg,#d0d1d3 0%,#6c6d70 40%,#a46a3e 65%,#5b5d60 100%)"></div>
  <div class="photo" role="img" aria-label="Glass facade building under dark overlay" style="left:377px;top:919px;width:126px;height:93px;background:linear-gradient(180deg,#1c1e23 0%,#22262e 60%,#1a1b1e 100%)">
    <svg class="abs" style="left:53px;top:36px" width="20" height="20" viewBox="0 0 20 20"><rect x="0.5" y="0.5" width="19" height="19" fill="none" stroke="#ffffff" stroke-opacity=".7"/><circle cx="9" cy="9" r="3" fill="none" stroke="#fff" stroke-width="1.3"/><path d="M11.2 11.2 L14 14" stroke="#fff" stroke-width="1.5"/></svg>
  </div>
  <div class="photo" role="img" aria-label="Dark blue clad office building corner" style="left:516px;top:919px;width:126px;height:93px;background:linear-gradient(170deg,#dcdddf 0%,#2e3a4e 35%,#26304a 80%,#3a3d42 100%)"></div>

  <div class="pager" style="left:607px;top:1021px"><svg width="6" height="8" viewBox="0 0 6 8"><path d="M4.5 1 L1.5 4 L4.5 7" fill="none" stroke="#333335" stroke-width="1.3"/></svg></div>
  <div class="pager" style="left:626px;top:1021px"><svg width="6" height="8" viewBox="0 0 6 8"><path d="M1.5 1 L4.5 4 L1.5 7" fill="none" stroke="#333335" stroke-width="1.3"/></svg></div>
</section>

<footer>
  <div class="footer">
    <div class="abs brand" style="left:99px;top:28px">Corvale Fitouts</div>
    <nav class="abs nav" style="right:99px;top:38px">
      <span>Home</span><span class="sep">/</span><span>Recent Projects</span><span class="sep">/</span><span>Our Services</span><span class="sep">/</span><span>Contact Us</span>
    </nav>
  </div>
  <p class="legal">© Copyright Corvale Fitouts Pty Ltd 2014</p>
  <div class="social" style="left:583px;top:1180px" aria-label="Social link"></div>
  <div class="social" style="left:604px;top:1180px" aria-label="Social link"></div>
  <div class="social" style="left:626px;top:1180px" aria-label="Social link"></div>
</footer>

</body>
</html>
```